Cycling Group adventures - weekly cycling with Ridewell Federation Coach for health and fitness

An A3 poster, like a flyer for information about a new cycling group. Lots of info on the poster so designed to be read close up and not needing to get attention from a long way off. All the info, yes there is a lot, is on the Word document attached. My colours are blue RGB 83, 108, 255 and orange 226, 83, 3.
There are three sections of info on the Word document the first is the most important.
The market is affluent and middle-aged.
So nothing wild or shouty. Nice, sophisticated, peaceful designs.
Photos really are background to the words. (I think I've accidentally downloaded some twice although I thought they were deleted.)

Industry/Entity Type

Health And Wellness

Font styles to use
Sans Serif

Requirements
Must have
• Clear font
Should not have
• Jazzy colours, lots of bubbles, flashy things or anything that looks like an advert for cheap jewellery/perfume/used cars.

```html
<!DOCTYPE html>
<html lang="en">
<head>
<meta charset="utf-8">
<title>Cycling with GearTwelve</title>
<link rel="stylesheet" href="https://fonts.googleapis.com/css2?family=Raleway:ital,wght@0,300;0,400;0,500;0,600;0,700;1,300&display=swap">
<style>
:root{
  --blue:#536cff;
  --blue-soft:#6f88ff;
  --blue-deep:#3f57e6;
  --orange:#e25303;
  --orange-soft:#e8702e;
  --orange-deep:#c44600;
  --white:#ffffff;
  --ink-light:rgba(255,255,255,.82);
}
*{margin:0;padding:0;box-sizing:border-box}
html,body{width:871px;height:1200px;overflow:hidden;background:#ececec}
body{font-family:"Raleway",sans-serif;color:var(--white)}
.poster{position:relative;width:871px;height:1200px;overflow:hidden;background:var(--blue)}
.backdrop{position:absolute;inset:0}
.header{position:absolute;left:0;top:0;width:614px;height:112px;background:var(--orange);padding:26px 18px 0 34px}
.header-title{font-size:28px;font-weight:300;letter-spacing:.3px;white-space:nowrap}
.header-title strong{font-weight:700}
.header-contact{margin-top:6px;text-align:right;font-size:18px;font-weight:700;letter-spacing:.6px}
.brand{position:absolute;left:644px;top:42px;display:flex;align-items:center;gap:8px;color:var(--blue);font-size:22px;font-weight:600}
.brand-dot{width:22px;height:22px;border-radius:50%;background:var(--blue)}
.facts{position:absolute;left:196px;top:140px;width:500px}
.fact{display:flex;margin-bottom:14px}
.fact-label{width:124px;flex:none;font-size:17px;font-weight:500;letter-spacing:.5px;line-height:1.15;text-transform:uppercase}
.fact-value{font-size:15px;font-weight:300;line-height:1.3;color:var(--ink-light)}
.fact-value em{display:block;font-size:14px;font-style:italic;margin-top:5px}
.fact-value.coach{font-size:13.4px;line-height:1.28;width:370px}
.faq{position:absolute;left:21px;top:530px;width:415px}
.faq h3{font-size:17px;font-weight:500;letter-spacing:.4px;text-transform:uppercase;line-height:1.15;margin-top:8px}
.faq h3 span{font-size:13.5px;font-weight:300;text-transform:none;letter-spacing:0;color:var(--ink-light)}
.faq p{font-size:13.5px;font-weight:300;line-height:1.24;color:var(--ink-light);margin-top:2px}
.other-band{position:absolute;left:435px;top:719px;width:436px;height:70px;background:var(--white);padding:22px 13px}
.other-band h2{color:var(--orange);font-size:23px;font-weight:700;letter-spacing:.6px}
.other{position:absolute;left:449px;top:818px;width:410px}
.other h4{font-size:15.5px;font-weight:500;line-height:1.12;margin-top:10px}
.other h4.first{margin-left:22px;margin-top:0}
.other p{font-size:13.4px;font-weight:300;line-height:1.24;color:var(--ink-light);margin-top:2px}
.other p.first{margin-left:22px}
</style>
</head>
<body>
<main class="poster">
  <svg class="backdrop" width="871" height="1200" viewBox="0 0 871 1200" aria-hidden="false">
    <defs>
      <linearGradient id="photoBlue" x1="0" y1="0" x2="1" y2="1"><stop offset="0" stop-color="#5b73f5"/><stop offset="1" stop-color="#4258d8"/></linearGradient>
      <linearGradient id="photoOrange" x1="0" y1="0" x2="1" y2="1"><stop offset="0" stop-color="#ee7a2a"/><stop offset="1" stop-color="#d24c05"/></linearGradient>
    </defs>
    <rect width="871" height="1200" fill="var(--blue)"/>
    <polygon role="img" aria-label="Photo of a smiling rider with her bike" points="0,112 173,112 173,420 0,330" fill="url(#photoBlue)"/>
    <polygon role="img" aria-label="Photo of a bicycle wheel in warm light" points="0,330 173,420 173,640 0,560" fill="url(#photoOrange)"/>
    <polygon role="img" aria-label="Photo of a rider in a cycling helmet" points="698,135 871,40 871,430 698,430" fill="url(#photoOrange)"/>
    <polygon role="img" aria-label="Photo of bikes on a roadside" points="698,430 871,430 871,720 698,720" fill="url(#photoBlue)"/>
    <polygon role="img" aria-label="Photo of a cyclist beside a stop sign" points="440,575 698,430 698,720 435,720" fill="url(#photoOrange)"/>
    <polygon points="0,440 173,500 440,575 435,1200 0,1200" fill="var(--orange)"/>
    <polygon points="0,1000 173,1090 173,1200 0,1200" fill="var(--blue)" opacity=".9"/>
    <polygon role="img" aria-label="Photo of riders having coffee after a session" points="250,1200 435,1110 435,1200" fill="url(#photoBlue)"/>
    <polygon points="173,112 698,112 698,430 440,575 173,423" fill="var(--blue-soft)"/>
    <polygon points="614,0 871,0 871,40 697,135 614,100" fill="var(--white)"/>
    <polygon points="442,112 582,112 578,130 560,180 545,140 442,130" fill="var(--orange-deep)"/>
    <polygon points="130,112 210,112 170,130" fill="var(--white)"/>
    <rect x="435" y="789" width="436" height="411" fill="var(--blue)"/>
    <polygon points="435,789 455,789 435,820" fill="var(--orange)"/>
    <polygon points="871,910 871,1090 720,1000" fill="var(--orange)" opacity=".85"/>
    <polygon points="460,789 555,789 480,800 482,830" fill="var(--white)"/>
  </svg>

  <header class="header">
    <h1 class="header-title"><strong>WHAT?</strong> – CYCLING WITH GEARTWELVE</h1>
    <p class="header-contact">WWW.GEARTWELVE.COM.AU | 0400 555 218</p>
  </header>
  <div class="brand"><span class="brand-dot"></span>GearTwelve</div>

  <section class="facts">
    <div class="fact"><div class="fact-label">Where?</div><div class="fact-value">_________________</div></div>
    <div class="fact"><div class="fact-label">When</div><div class="fact-value">Date______Day_______<em>Weekly 60 min (or so) sessions for 5 weeks.</em></div></div>
    <div class="fact"><div class="fact-label">Whom?</div><div class="fact-value">Up to 7 participants</div></div>
    <div class="fact"><div class="fact-label">Booking essential?</div><div class="fact-value">Yes, for purposes of insurance</div></div>
    <div class="fact"><div class="fact-label">Who coaches it?</div><div class="fact-value coach">Daniel Hartley, Ridewell Federation Accredited Coach, coach to the Junior Emerging Talent squad of Qld, ride leader of Ridewell Federation's Roll Out and Pedal On programmes and has an Exercise Physiology &amp; Biomechanics degree tutored by Owen Pratt who co-founded the Northgate Sports Medical Centre. Daniel can talk whilst cycling uphill but will limit this to useful things.</div></div>
  </section>

  <section class="faq">
    <h3>Gender of rider?<br>Is it competitive?</h3>
    <p>Either/both though this time-frame is female dominated. No. No it isn't</p>
    <h3>Might I get left behind? <span>No. No you won't.</span></h3>
    <h3>Clothing? –</h3>
    <p>Close fitting sporting clothing is fine if you are not a 'lycra' wearer. Full pro kit welcomed too if you like that. So long as it's comfortable and won't get caught in moving parts. Helmet? Australian law so it's essential.</p>
    <h3>Bike? –</h3>
    <p>All types welcomed. If you are on a classic beach cruiser or town bike weighing 20kg it does make it harder, though I do work with Joanne Keller and that's her bike of choice in her post-World Champion era. I'll help make sure your bike fits you.</p>
    <h3>Ability level?</h3>
    <p>Aimed at people who can ride a bike including moderate inclines but wouldn't currently have the confidence to do a 20km ride. Also aimed at people who may be able to do 20km but would like it to be easier.</p>
    <h3>Will it be a mixed ability? –</h3>
    <p>Always. I adapt this in every session I do as needs demand.</p>
    <h3>How much? <span>$129 for the 5 weeks.</span></h3>
    <h3>Do we have coffee afterwards?</h3>
    <p>If you like? It is fairly traditional. Also it is a good time to ask if you enjoyed it, achieved in the session what you wanted and what you'd like to work on next, whatever that may be.</p>
  </section>

  <div class="other-band"><h2>OTHER STUFF:</h2></div>
  <section class="other">
    <h4 class="first">I'd like a different day and time</h4>
    <p class="first">Give me a ring we'll work out a plan</p>
    <h4>My husband insists he could improve my cycling as he rides a lot</h4>
    <p>It is an option. It could work well. Anecdotal evidence suggest some of these are less successful than others.</p>
    <h4>I'm seriously fit and can do 55km in 2 hours and want to be even quicker</h4>
    <p>This is good, give me a ring we'll work out a plan.</p>
    <h4>I, however, can hardly ride at all and haven't been on a bike in a while –</h4>
    <p>I also present Basics from Ridewell Federation. Call for details or see the Ridewell Federation website for details. Give me a ring and we'll work out a plan.</p>
    <h4>I want to do this</h4>
    <p>Phone my number 0400 555 218 or find my website and click Contact Us if you prefer. Either or.</p>
  </section>
</main>
</body>
</html>
```